The Pixel Tap Business card.

A Simple card with our Logo and contact information. To give to investors and other professionals.

We are a nerd themed bar.
our target market is young professionals age 21+ but the real purpose of this business card is to present to potential investors and other professionals with our contact information. as we are still looking for funding before we start up.

I am partial to green and my partner likes red we are open to iteration.

Target Market(s)

Investors

Industry/Entity Type

Business

Contact Information for Business Card

Martin Hale (225) 730-6192 kent.h4711@mailnest.test Glen Porter (225) 968-5037 glenp318@mailnest.test

Font styles to use
Serif

Requirements
Nice to have
• Keep it simple but not boring.
• Use the Logos but feel free to edit them to match theme/colors.
• Keep the back clean and use one of the Logos.

```html
<!DOCTYPE html>
<html lang="en">
<head>
<meta charset="utf-8">
<title>The Pixel Tap – Business Card</title>
<link rel="stylesheet" href="https://fonts.googleapis.com/css2?family=Open+Sans:wght@400;700;800&display=swap">
<style>
  :root {
    --page-bg: #e9e7e4;
    --steel-light: #f2f2f2;
    --steel-mid: #d4d4d4;
    --steel-dark: #b9b9b9;
    --ink: #111111;
    --panel-black: #050505;
    --accent-green: #21c12b;
    --accent-red: #e0283a;
    --text-white: #ffffff;
  }
  * { box-sizing: border-box; margin: 0; padding: 0; }
  html, body {
    width: 1200px; height: 1120px; overflow: hidden;
    background: var(--page-bg);
    font-family: "Open Sans", Arial, sans-serif;
  }
  .canvas {
    width: 1200px; height: 1120px;
    display: flex; flex-direction: column; align-items: center; justify-content: center;
    gap: 56px;
  }
  .card {
    position: relative;
    width: 860px; height: 492px;
    overflow: hidden;
    background:
      repeating-linear-gradient(90deg, rgba(255,255,255,.18) 0 1px, rgba(0,0,0,.03) 1px 3px),
      linear-gradient(160deg, var(--steel-light) 0%, var(--steel-mid) 55%, var(--steel-dark) 100%);
    box-shadow: 0 10px 30px rgba(0,0,0,.25);
  }
  /* Back of card: name only */
  .card-back .brand {
    position: absolute; inset: 0;
    display: flex; align-items: center; justify-content: center; gap: 18px;
  }
  .brand-dot {
    width: 34px; height: 34px; border-radius: 50%;
    background: var(--accent-red);
  }
  .brand-name {
    font-weight: 800; color: var(--ink);
    font-size: 68px; letter-spacing: 1px; text-transform: uppercase;
  }
  /* Front of card: contacts */
  .card-front .panel {
    position: absolute; inset: 0;
  }
  .card-front .brand {
    position: absolute; left: 40px; top: 0; width: 360px; height: 100%;
    display: flex; align-items: center; justify-content: center; gap: 14px;
  }
  .card-front .brand-name { font-size: 48px; line-height: 1.05; text-align: left; }
  .card-front .brand-dot { width: 26px; height: 26px; flex: none; }
  .contacts {
    position: absolute; right: 60px; top: 72px;
    text-align: right; color: var(--text-white);
  }
  .person + .person { margin-top: 34px; }
  .person-name {
    color: var(--accent-green); font-weight: 700;
    font-size: 27px; text-transform: uppercase; margin-bottom: 6px;
  }
  .contact-line {
    display: flex; align-items: center; justify-content: flex-end; gap: 10px;
    font-size: 21px; line-height: 1.5;
  }
  .contact-line svg { width: 18px; height: 18px; flex: none; }
</style>
</head>
<body>
<main class="canvas">
  <section class="card card-back" aria-label="Card back">
    <div class="brand">
      <span class="brand-dot"></span>
      <span class="brand-name">The Pixel Tap</span>
    </div>
  </section>

  <section class="card card-front" aria-label="Card front">
    <svg class="panel" viewBox="0 0 860 492" width="860" height="492" aria-hidden="true">
      <circle cx="742" cy="250" r="330" fill="var(--accent-green)"/>
      <circle cx="750" cy="248" r="330" fill="#ffffff"/>
      <circle cx="760" cy="246" r="330" fill="var(--panel-black)"/>
    </svg>

    <div class="brand">
      <span class="brand-dot"></span>
      <span class="brand-name">The<br>Pixel Tap</span>
    </div>

    <div class="contacts">
      <div class="person">
        <p class="person-name">Martin Hale</p>
        <p class="contact-line">
          <svg viewBox="0 0 24 24"><path fill="var(--accent-green)" d="M6.6 10.8a15 15 0 0 0 6.6 6.6l2.2-2.2c.3-.3.7-.4 1-.2 1.1.4 2.3.6 3.6.6.6 0 1 .4 1 1V20c0 .6-.4 1-1 1A17 17 0 0 1 3 4c0-.6.4-1 1-1h3.5c.6 0 1 .4 1 1 0 1.3.2 2.5.6 3.6.1.3 0 .7-.2 1z"/></svg>
          (225) 730-6192
        </p>
        <p class="contact-line">
          <svg viewBox="0 0 24 24"><path fill="var(--accent-green)" d="M2 6h20v12H2z"/><path fill="none" stroke="var(--panel-black)" stroke-width="1.8" d="M2 6l10 7 10-7"/></svg>
          kent.h4711@mailnest.test
        </p>
      </div>
      <div class="person">
        <p class="person-name">Glen Porter</p>
        <p class="contact-line">
          <svg viewBox="0 0 24 24"><path fill="var(--accent-green)" d="M6.6 10.8a15 15 0 0 0 6.6 6.6l2.2-2.2c.3-.3.7-.4 1-.2 1.1.4 2.3.6 3.6.6.6 0 1 .4 1 1V20c0 .6-.4 1-1 1A17 17 0 0 1 3 4c0-.6.4-1 1-1h3.5c.6 0 1 .4 1 1 0 1.3.2 2.5.6 3.6.1.3 0 .7-.2 1z"/></svg>
          (225) 968-5037
        </p>
        <p class="contact-line">
          <svg viewBox="0 0 24 24"><path fill="var(--accent-green)" d="M2 6h20v12H2z"/><path fill="none" stroke="var(--panel-black)" stroke-width="1.8" d="M2 6l10 7 10-7"/></svg>
          glenp318@mailnest.test
        </p>
      </div>
    </div>
  </section>
</main>
</body>
</html>
```